Brivora Collective Business Card Design

We need a business card design for Brivora Collective. We are a healthcare recruiting, wellness and education company. We partner with medical facilities to find quality candidates. We also offer free wellness courses.
The final design should communicate an emphasis on recruiting and wellness
The main purpose of the business card is to utilized it for networking events, give to hospitals, executives, VCs surgery centers and clinics. I want it to be sleek, clean, use of our brand colors and professional.

```html
<!DOCTYPE html>
<html lang="en">
<head>
<meta charset="utf-8">
<title>Brivora Collective – Business Card</title>
<link rel="stylesheet" href="https://fonts.googleapis.com/css2?family=Open+Sans:wght@400;600;700&display=swap">
<style>
  :root {
    --backdrop: #222222;
    --brand-teal: #0d5b52;
    --brand-deep: #0f5c56;
    --brand-green: #22a35e;
    --card-white: #ffffff;
    --ink: #1c1c1c;
    --ghost: #e6ebeb;
  }
  * { box-sizing: border-box; margin: 0; padding: 0; }
  html, body {
    width: 1200px; height: 780px; overflow: hidden;
    background: var(--backdrop);
    font-family: "Open Sans", Arial, sans-serif;
  }
  .stage {
    position: relative; width: 1200px; height: 780px;
    display: flex; align-items: center; justify-content: center; gap: 44px;
  }
  .card {
    position: relative; width: 530px; height: 303px; overflow: hidden;
  }
  /* Front */
  .card-front { background: var(--card-white); }
  .ghost-shape {
    position: absolute; left: 70px; top: 40px; width: 200px; height: 200px;
    background: var(--ghost); border-radius: 22px;
  }
  .name-bar {
    position: absolute; left: 0; top: 28px; width: 12px; height: 44px;
    background: var(--brand-teal);
  }
  .holder { position: absolute; left: 26px; top: 26px; }
  .holder-name {
    font-weight: 700; font-size: 25px; color: var(--brand-teal); line-height: 1.1;
  }
  .holder-role { font-size: 12px; color: var(--ink); margin-top: 2px; }
  .brand {
    position: absolute; display: flex; align-items: center; gap: 10px;
  }
  .card-front .brand { right: 40px; top: 118px; }
  .brand-square {
    width: 26px; height: 26px; border-radius: 4px; background: var(--brand-teal);
  }
  .brand-name {
    font-weight: 600; font-size: 28px; color: var(--brand-teal); letter-spacing: -0.3px;
  }
  .contact {
    position: absolute; right: 36px; bottom: 24px;
    list-style: none; text-align: right;
  }
  .contact li {
    display: flex; justify-content: flex-end; align-items: center; gap: 8px;
    font-size: 13.5px; color: var(--ink); line-height: 22px;
  }
  .contact svg { width: 13px; height: 13px; fill: var(--brand-teal); }
  .corner-bar {
    position: absolute; right: 0; bottom: 0; width: 12px; height: 80px;
    background: var(--brand-teal);
  }
  /* Back */
  .card-back { background: var(--brand-deep); }
  .card-back .brand {
    left: 0; right: 0; top: 0; bottom: 0; justify-content: center;
  }
  .card-back .brand-square { width: 34px; height: 34px; background: var(--brand-green); }
  .card-back .brand-name { font-size: 36px; color: var(--brand-green); }
</style>
</head>
<body>
<main class="stage">
  <section class="card card-front">
    <div class="ghost-shape" aria-hidden="true"></div>
    <div class="name-bar"></div>
    <div class="holder">
      <p class="holder-name">Maren Kestrel</p>
      <p class="holder-role">Founder</p>
    </div>
    <div class="brand">
      <span class="brand-square"></span>
      <span class="brand-name">Brivora Collective</span>
    </div>
    <ul class="contact">
      <li>(555) 214-0187
        <svg viewBox="0 0 24 24" aria-hidden="true"><path d="M6.6 10.8a15.1 15.1 0 0 0 6.6 6.6l2.2-2.2a1 1 0 0 1 1-.25 11.4 11.4 0 0 0 3.6.57 1 1 0 0 1 1 1V20a1 1 0 0 1-1 1A17 17 0 0 1 3 4a1 1 0 0 1 1-1h3.5a1 1 0 0 1 1 1c0 1.25.2 2.45.57 3.57a1 1 0 0 1-.25 1z"/></svg>
      </li>
      <li>www.brivoracollective.com
        <svg viewBox="0 0 24 24" aria-hidden="true"><path d="M12 2a10 10 0 1 0 0 20 10 10 0 0 0 0-20zm6.9 6h-2.9a15.7 15.7 0 0 0-1.4-3.6A8 8 0 0 1 18.9 8zM12 4c.8 1.2 1.5 2.5 1.9 4h-3.8c.4-1.5 1.1-2.8 1.9-4zM4.3 14a8.2 8.2 0 0 1 0-4h3.4a16.5 16.5 0 0 0 0 4zm.8 2h2.9c.3 1.3.8 2.5 1.4 3.6A8 8 0 0 1 5.1 16zM8 8H5.1a8 8 0 0 1 4.3-3.6C8.8 5.5 8.3 6.7 8 8zm4 12c-.8-1.2-1.5-2.5-1.9-4h3.8c-.4 1.5-1.1 2.8-1.9 4zm2.3-6H9.7a14.7 14.7 0 0 1 0-4h4.6a14.7 14.7 0 0 1 0 4zm.3 5.6c.6-1.1 1.1-2.3 1.4-3.6h2.9a8 8 0 0 1-4.3 3.6zm1.7-5.6a16.5 16.5 0 0 0 0-4h3.4a8.2 8.2 0 0 1 0 4z"/></svg>
      </li>
      <li>hello@brivoracollective.com
        <svg viewBox="0 0 24 24" aria-hidden="true"><path d="M3 5h18a1 1 0 0 1 1 1v12a1 1 0 0 1-1 1H3a1 1 0 0 1-1-1V6a1 1 0 0 1 1-1zm9 7.2L4.4 7H4v.9l8 5.4 8-5.4V7h-.4z"/></svg>
      </li>
    </ul>
    <div class="corner-bar"></div>
  </section>

  <section class="card card-back">
    <div class="brand">
      <span class="brand-square"></span>
      <span class="brand-name">Brivora Collective</span>
    </div>
  </section>
</main>
</body>
</html>
```